sailbuddies Website for children with diabilities

Hi, we are looking for a new website design for our community service "sailbuddies". Sailbuddies gives children who suffer from diseases or disabilities a week off on a Boat to give the children new hope and an unforgettable experience.

The current website is really old and we want to have a new one.
Please feel free to discover our website under http://sailbuddies-example.at/.
We have several company sponsors which are very important to us.

The Website has to be a Bootstrap Design (Version 4.4 or higher) [NOT Wordpress, Joomla, other CMS]

Target Market(s)

no target market. we like to inform our communities about our service.

Industry/Entity Type

community service for children with disabilities

Coding

Coded - Design and coding required

Number of Pages Required

4 page

Font styles to use
Sans Serif

Colors
0054AA
0677BA
7BADD7
CADEEF
E8F1F8
0094D4
00A9DD
6FCCEA
C7EBF8
E9F6FB

Requirements
Must have
• About, Sponsors, Information about cruises
Nice to have
• Gallery

```html
<!DOCTYPE html>
<html lang="de">
<head>
<meta charset="utf-8">
<title>Sailbuddies – Kindern mit Behinderungen helfen</title>
<link href="https://fonts.googleapis.com/css2?family=Montserrat:wght@400;500;600&family=Outfit:wght@500;600;700&display=swap" rel="stylesheet">
<style>
:root{
  --navy:#141c55;
  --navy-deep:#111a52;
  --navy-panel:#2a3574;
  --ink:#1b2466;
  --light-panel:#dde2ec;
  --white:#ffffff;
  --muted:#8f97c4;
  --sea-1:#0d6fa8;
  --sea-2:#1b8fc4;
  --sea-3:#3aa9d6;
}
*{box-sizing:border-box;margin:0;padding:0}
html,body{width:1200px;height:2705px;overflow:hidden}
body{font-family:"Montserrat",sans-serif;color:var(--ink);background:var(--white);position:relative}
h1,h2,h3{font-family:"Outfit",sans-serif}

/* Header */
.site-header{position:absolute;top:0;left:0;width:1200px;height:84px;background:var(--navy)}
.brand-box{position:absolute;left:76px;top:0;width:115px;height:116px;background:var(--white);border:2px solid var(--navy);border-top:none;border-radius:0 0 8px 8px;display:flex;align-items:center;justify-content:center}
.brand-mark{width:76px;height:76px;border-radius:50%;background:var(--navy)}
.brand-name{position:absolute;left:213px;top:42px;font-family:"Outfit",sans-serif;font-weight:500;font-size:25px;color:var(--white);letter-spacing:.5px}
.main-nav{position:absolute;right:76px;top:34px;display:flex;gap:29px;font-size:15px;font-weight:500}
.main-nav a{color:var(--muted);text-decoration:none}
.main-nav a.active{color:var(--white)}

/* Hero */
.hero{position:absolute;top:84px;left:0;width:1200px;height:481px;background:var(--white)}
.hero-photo{position:absolute;top:0;right:0;width:800px;height:481px;
  background:linear-gradient(90deg,rgba(255,255,255,1) 0%,rgba(255,255,255,0) 30%),
  linear-gradient(160deg,var(--sea-3) 0%,var(--sea-2) 40%,var(--sea-1) 100%)}
.hero h1{position:absolute;left:74px;top:96px;font-size:66px;line-height:64px;font-weight:700;color:var(--navy);width:520px}
.hero-quote{position:absolute;left:75px;top:325px;width:440px;font-size:19px;line-height:22px;color:var(--navy)}
.hero-author{position:absolute;left:75px;top:414px;font-size:15px;font-weight:600;color:var(--navy)}

/* About split */
.about-split{position:absolute;top:565px;left:0;width:1200px;height:422px;display:flex}
.about-col{width:600px;height:422px;padding:52px 43px 0 75px}
.about-col.dark{background:linear-gradient(180deg,#2f3b7c,#27336f);color:var(--white)}
.about-col.light{background:var(--light-panel);color:var(--ink);padding-left:43px}
.about-col h2{font-size:38px;font-weight:500;margin-bottom:30px}
.about-col p{font-size:17px;line-height:25.3px}

/* Practice */
.practice{position:absolute;top:987px;left:0;width:1200px;height:546px}
.practice-photo{position:absolute;left:76px;top:47px;width:337px;height:401px;background:linear-gradient(160deg,#c9d6e2,#e05a2a 60%,#324a66)}
.practice h2{position:absolute;left:460px;top:50px;width:680px;font-size:38px;line-height:47px;font-weight:500}
.practice p{position:absolute;left:460px;top:168px;width:675px;font-size:17px;line-height:25.3px}

/* Goals */
.goals{position:absolute;top:1533px;left:0;width:1200px;height:462px;background:var(--navy-deep);color:var(--white)}
.goals h2{position:absolute;left:75px;top:50px;font-size:38px;font-weight:500}
.goal-card{position:absolute;width:337px;height:133px;border:2px solid #3b4585;display:flex;align-items:center;padding:0 18px;gap:18px;font-size:17px;line-height:25px}
.goal-card svg{flex:none}

/* Achieved */
.achieved{position:absolute;top:1995px;left:0;width:1200px;height:430px}
.achieved h2{position:absolute;left:76px;top:52px;font-size:38px;font-weight:500}
.achieved p{position:absolute;left:76px;top:123px;width:515px;font-size:17px;line-height:25.3px}
.achieved-photo{position:absolute;left:609px;top:47px;width:516px;height:331px;background:linear-gradient(180deg,#dfe6ea 0%,#f5f5f2 40%,#5f9fcc 70%,#3f86bd 100%)}

/* Footer */
.site-footer{position:absolute;top:2425px;left:0;width:1200px;height:280px;background:var(--navy);color:var(--white)}
.footer-brand{position:absolute;left:76px;top:50px;display:flex;align-items:center;gap:20px}
.footer-brand .brand-mark{width:70px;height:70px;background:transparent;border:2px solid var(--white)}
.footer-brand span{font-family:"Outfit",sans-serif;font-weight:500;font-size:27px}
.footer-col{position:absolute;top:68px}
.footer-col h3{font-family:"Montserrat",sans-serif;font-size:14px;font-weight:600;margin-bottom:20px}
.footer-col a{display:block;color:var(--muted);font-size:14px;line-height:24.5px;text-decoration:none}
.footer-rule{position:absolute;left:76px;top:230px;width:1049px;height:1px;background:#2f3878}
.footer-copy{position:absolute;left:76px;top:252px;font-size:10px;color:var(--muted)}
</style>
</head>
<body>

<header class="site-header">
  <div class="brand-box"><div class="brand-mark"></div></div>
  <div class="brand-name">Sailbuddies</div>
  <nav class="main-nav">
    <a class="active" href="#">Home</a>
    <a href="#">Sponsors</a>
    <a href="#">Fleet Info 2022</a>
    <a href="#">About</a>
    <a href="#">Contact</a>
  </nav>
</header>

<section class="hero">
  <div class="hero-photo" role="img" aria-label="Luftaufnahme kleiner Segelboote auf blauem Meer"></div>
  <h1>Kindern mit Behinderungen helfen</h1>
  <p class="hero-quote">Wir Können die Windrichtung nicht bestimmen, aber wir können die Segel rictig setzen!</p>
  <p class="hero-author">Marcus Velarius</p>
</section>

<section class="about-split">
  <div class="about-col dark">
    <h2>Wer sind wir</h2>
    <p>Wir sind ausgebildete SozialpädagogInnen und erfahrene SkipperInnen,&nbsp; die sich ehrenamtlich im Verein Sailbuddies engagieren und alljährlich für sozial benachteiligte Kinder und Jugendliche, aus dem oberösterreichischen Zentralraum, eine Flotte organisieren und die dafür notwendigen finanziellen Mittel aufstellen.</p>
  </div>
  <div class="about-col light">
    <h2>Was wir wollen</h2>
    <p>Wir wollen Kindern und Jugendlichen, die es im Leben nicht immer leicht haben, eine unvergessliche Woche in Kroatien ermöglichen. Denn genau dieses gemeinsame Erlebnis vermittelt den Kindern und Jugendlichen neue Lebensfreude und Perspektiven für ihre Zukunft.&nbsp; Durch die Reflexion und auch die Betreuung danach in den einzelnen Einrichtungen, können die Kinder und Jugendlichen noch lange an diesem Erlebnis zehren. Diese Nachhaltigkeit schafft zahlreiche pädagogische Anknüpfungspunkte, die für die Zielerreichung eine wertvolle Grundlage darstellen.</p>
  </div>
</section>

<section class="practice">
  <div class="practice-photo" role="img" aria-label="Junge beim Segeln mit Schwimmweste"></div>
  <h2>Praktische Umsetzung der pädagogischen Überlegungen</h2>
  <p>Die TeilnehmerInnen werden bewusst zu Tätigkeiten beim Segeln herangezogen. Es gibt Verantwortlichkeiten für verschiedenste Aufgaben im täglichen Zusammenleben. Ein Koch- und Putzplan soll dazu beitragen, Verantwortung gegenüber der Gruppe zu übernehmen. Die Tatsache, ein Segelschiff alleine zu steuern, erfüllt so manchen mit großem Stolz. Wiederkehrende Tätigkeiten am Schiff erfordern die Beteiligung jedes Crewmitglieds. So wird allen das Gefühl vermittelt, eine Bedeutung für die Gemeinschaft zu haben und jede/r lernt dabei, diese Verantwortung nach eigener Möglichkeit auch zu tragen. Sailbuddies bietet ein ideales Übungsfeld für soziales Lernen. Die intensive Auseinandersetzung mit anderen und der Gruppe auf engstem Raum, bietet verschiedenste Möglichkeiten, sich im Umgang mit Mitmenschen zu erproben. All diese Erfahrungen können zu einer Aufwertung ihrer selbst führen.</p>
</section>

<section class="goals">
  <h2>Projektziele</h2>
  <div class="goal-card" style="left:76px;top:131px">
    <svg width="82" height="82" viewBox="0 0 82 82" fill="#fff"><circle cx="10" cy="10" r="5"/><rect x="5" y="17" width="10" height="12" rx="2"/><circle cx="72" cy="10" r="5"/><rect x="67" y="17" width="10" height="12" rx="2"/><circle cx="10" cy="60" r="5"/><rect x="5" y="67" width="10" height="12" rx="2"/><circle cx="72" cy="60" r="5"/><rect x="67" y="67" width="10" height="12" rx="2"/><rect x="20" y="22" width="42" height="3"/><rect x="20" y="72" width="42" height="3"/><rect x="26" y="32" width="20" height="16" rx="2"/><rect x="38" y="42" width="20" height="16" rx="2" fill="none" stroke="#fff" stroke-width="3"/></svg>
    <span>Stärkung des Selbstwertgefühls und der sozialen KompetenzG</span>
  </div>
  <div class="goal-card" style="left:432px;top:131px">
    <svg width="64" height="82" viewBox="0 0 64 82" fill="#fff"><rect x="2" y="2" width="30" height="26" rx="2"/><circle cx="56" cy="30" r="6"/><path d="M30 34 L46 34 L40 52 L48 78 L40 80 L30 56 L22 80 L14 78 L24 46 Z"/><rect x="10" y="28" width="20" height="6"/></svg>
    <span>Verantwortung für sich selbst und andere übernehmen</span>
  </div>
  <div class="goal-card" style="left:788px;top:131px">
    <svg width="72" height="82" viewBox="0 0 72 82" fill="#fff"><circle cx="20" cy="16" r="8"/><circle cx="52" cy="16" r="8"/><path d="M8 30 L30 30 L38 44 L46 30 L64 30 L66 80 L58 80 L56 48 L36 58 L16 48 L14 80 L6 80 Z"/></svg>
    <span>Üben von Toleranz</span>
  </div>
  <div class="goal-card" style="left:76px;top:284px">
    <svg width="82" height="82" viewBox="0 0 82 82" fill="#fff"><circle cx="41" cy="22" r="18" fill="none" stroke="#fff" stroke-width="4"/><path d="M41 12 V22 L49 28" stroke="#fff" stroke-width="4" fill="none"/><circle cx="12" cy="52" r="6"/><rect x="2" y="62" width="22" height="16" rx="3"/><circle cx="70" cy="52" r="6"/><rect x="58" y="62" width="22" height="16" rx="3"/><rect x="26" y="66" width="30" height="4"/></svg>
    <span>Erarbeiten gewaltfreier Konfliktlösungsstrateg ien</span>
  </div>
  <div class="goal-card" style="left:432px;top:284px">
    <svg width="64" height="82" viewBox="0 0 64 82" fill="#fff"><circle cx="32" cy="20" r="11" fill="none" stroke="#fff" stroke-width="4"/><path d="M26 20 L31 25 L39 15" stroke="#fff" stroke-width="3" fill="none"/><rect x="30" y="0" width="4" height="5"/><path d="M4 40 L30 44 L30 80 L4 76 Z M60 40 L34 44 L34 80 L60 76 Z"/></svg>
    <span>Erlebnisorientiertes Lernen</span>
  </div>
</section>

<section class="achieved">
  <h2>Erreichte Ziele</h2>
  <p>Durch das Erlebnis einer gemeinsamen Segelwoche schafft die "Sailbuddies Flotte" ideale Bedingungen, unter denen die Leitziele wie soziale Integration und pädagogische Weiterentwicklung der Kinder auf konkrete, effiziente und professionelle Weise, und mit nachhaltiger Wirkung umgesetzt wurden.</p>
  <div class="achieved-photo" role="img" aria-label="Zwei Kinder in einem kleinen Segelboot auf dem Meer"></div>
</section>

<footer class="site-footer">
  <div class="footer-brand"><div class="brand-mark"></div><span>Sailbuddies</span></div>
  <div class="footer-col" style="left:520px">
    <h3>Company</h3>
    <a href="#">About</a><a href="#">Services</a><a href="#">Fleet Info 2022</a><a href="#">Contact</a>
  </div>
  <div class="footer-col" style="left:773px">
    <h3>Follow Us</h3>
    <a href="#">Facepage</a><a href="#">Snapgram</a><a href="#">Chirper</a>
  </div>
  <div class="footer-col" style="left:1030px;top:71px">
    <h3>Our Policies</h3>
    <a href="#">Privacy Policy</a><a href="#">Terms of Use</a>
  </div>
  <div class="footer-rule"></div>
  <p class="footer-copy">© 2022 Sailbuddies. All Rights Reserved</p>
</footer>

</body>
</html>
```